Packaging and Logo for upscale skincare line

The name of the brand is Rosalind Rosalind. We would like a logo that's a mirror image of there name Rosalind. Packaging design for three signature products, face cream, body cream, and an aerosol spf. The face cream should be about 1/3 of the size of the body cream, in similarly shaped containers with twist-off lids, and a spatula for the face cream. And the spf should be a taller, slimmer, bottle with removable cap and aerosol spray.
Updates

Low design quality

Industry/Entity Type

Skin Care

Logo Text

Rosalind

Colors
2a71b2
3176b5
85acd3
ffffff

Requirements
Must have
• N/A
Nice to have
• Would like the logo Rosalind Rosalind to be a single Rosalind in a mirror image. We also want the packaging to are in a deep blue ocean color with either a chrome or satin finish and the logo/wording on it to be almost like a pearl color. See colors attached.

```html
<!DOCTYPE html>
<html lang="en">
<head>
<meta charset="utf-8">
<title>Rosalind Face Cream Packaging</title>
<link rel="stylesheet" href="https://fonts.googleapis.com/css2?family=Lato:wght@300;400&family=PT+Serif&display=swap">
<style>
  :root {
    --page-bg: #f3f4f5;
    --pearl-white: #ffffff;
    --ocean-blue: #2a6eae;
    --side-stripe: #5b8fc3;
    --dot-field: #4f86bd;
    --rule: #a9c4e0;
  }
  * { margin: 0; padding: 0; box-sizing: border-box; }
  html, body {
    width: 1200px;
    height: 1200px;
    overflow: hidden;
    background: var(--page-bg);
  }
  .package-face {
    position: absolute;
    left: 180px;
    top: 170px;
    width: 840px;
    height: 860px;
    background: var(--pearl-white);
    box-shadow: 0 10px 40px rgba(0, 0, 0, 0.08);
    overflow: hidden;
  }
  .label-band {
    position: absolute;
    left: 0;
    top: 378px;
    width: 840px;
    height: 482px;
    background: var(--ocean-blue);
  }
  .side-stripe {
    position: absolute;
    right: 0;
    top: 0;
    width: 90px;
    height: 100%;
    background: var(--side-stripe);
  }
  .dot-field {
    position: absolute;
    left: 0;
    top: 296px;
    width: 170px;
    height: 186px;
    background: var(--dot-field);
  }
  .label-text {
    position: absolute;
    left: 0;
    top: 0;
    width: 840px;
    text-align: center;
    color: var(--pearl-white);
  }
  .brand-name {
    position: absolute;
    left: 0;
    width: 100%;
    top: 80px;
    font-family: "Lato", sans-serif;
    font-weight: 400;
    font-size: 48px;
    letter-spacing: 5px;
    line-height: 1;
  }
  .brand-rule {
    position: absolute;
    left: 300px;
    top: 150px;
    width: 240px;
    height: 1px;
    background: var(--rule);
  }
  .product-name {
    position: absolute;
    left: 0;
    width: 100%;
    top: 246px;
    font-family: "Lato", sans-serif;
    font-weight: 300;
    font-size: 34px;
    letter-spacing: 4px;
    line-height: 1;
  }
  .product-benefits {
    position: absolute;
    left: 0;
    width: 100%;
    top: 298px;
    font-family: "PT Serif", serif;
    font-size: 18px;
    letter-spacing: 0.5px;
    line-height: 1;
  }
  .benefit-dot {
    display: inline-block;
    width: 6px;
    height: 6px;
    border-radius: 50%;
    background: var(--pearl-white);
    margin: 0 8px;
    vertical-align: middle;
  }
</style>
</head>
<body>
  <div class="package-face">
    <div class="label-band">
      <div class="side-stripe"></div>
      <div class="dot-field" role="img" aria-label="Soft dotted pattern decoration in light blue"></div>
      <div class="label-text">
        <div class="brand-name">Rosalind</div>
        <div class="brand-rule"></div>
        <div class="product-name">Face Cream</div>
        <div class="product-benefits">Purify<span class="benefit-dot"></span>Detox<span class="benefit-dot"></span>moisturize</div>
      </div>
    </div>
  </div>
</body>
</html>
```